Zarqa Fowl "The Tender Path"

I need a business card design and a logo design for my business. It's a delivery business of halal poultry (chicken). I would the business card to include the following information.
-business name: Zarqa Fowl
-business tag line: "The Tender Path"
Name: Tariq Moussef
Contact number: 07812450937
E-mail: zarqa_fowl@mailbox-example.com
Website: www.zarqafowl-example.com
Also need a business logo also included relating to the business.
I would like it professional yet creative. Something original. I want it to have 2 main colours included.
I want it to have a middle Eastern/ Arabic look if possible.
Thanks :)
Target Market(s)
Butchers
Restaurants
Industry/Entity Type
Business
Contact Information for Business Card
Business name: Zarqa fowl
Business tag line: "The Tender Path"
E-mail: zarqa_fowl@mailbox-example.com
Name: Tariq Moussef

```html
<!DOCTYPE html>
<html lang="en">
<head>
<meta charset="utf-8">
<title>Zarqa Fowl — Business Card</title>
<link rel="stylesheet" href="https://fonts.googleapis.com/css2?family=Michroma&display=swap">
<style>
  :root {
    --backdrop: #e9e6dc;
    --card: #fbfaf4;
    --teal: #3fb59c;
    --teal-soft: #5cc2ab;
    --rose: #c8346a;
    --rose-pattern: #e7a6b9;
  }
  * { margin: 0; padding: 0; box-sizing: border-box; }
  html, body {
    width: 1200px;
    height: 758px;
    overflow: hidden;
    background: var(--backdrop);
  }
  .canvas {
    position: relative;
    width: 1200px;
    height: 758px;
  }
  .card {
    position: absolute;
    left: 80px;
    top: 79px;
    width: 1040px;
    height: 600px;
    background: var(--card);
    box-shadow: 0 2px 8px rgba(0,0,0,0.12);
    font-family: "Michroma", sans-serif;
  }
  .card__frame {
    position: absolute;
    inset: 0;
    width: 100%;
    height: 100%;
  }
  .card__tagline {
    position: absolute;
    right: 70px;
    top: 62px;
    font-size: 30px;
    color: var(--teal-soft);
    letter-spacing: 0.5px;
  }
  .brand {
    position: absolute;
    left: 120px;
    top: 250px;
    display: flex;
    align-items: center;
    gap: 14px;
  }
  .brand__mark {
    width: 22px;
    height: 22px;
    border-radius: 50%;
    background: var(--teal);
  }
  .brand__name {
    font-size: 34px;
    color: var(--rose);
  }
  .card__person {
    position: absolute;
    left: 560px;
    top: 250px;
    font-size: 28px;
    color: var(--rose);
    letter-spacing: 0.5px;
  }
  .contact {
    position: absolute;
    left: 520px;
    top: 400px;
    list-style: none;
    font-size: 16px;
    line-height: 1.55;
    color: var(--teal);
  }
</style>
</head>
<body>
<main class="canvas">
  <section class="card" aria-label="Zarqa Fowl business card">
    <svg class="card__frame" viewBox="0 0 1040 600" aria-hidden="false">
      <g role="img" aria-label="Pink Arabic-style diamond pattern border">
        <path fill="var(--rose-pattern)" fill-rule="evenodd"
              d="M18 18 H1022 V582 H18 Z M44 44 V556 H996 V44 Z"/>
      </g>
      <rect x="13" y="13" width="1014" height="574" fill="none" stroke="var(--teal)" stroke-width="2"/>
      <rect x="52" y="52" width="936" height="496" fill="none" stroke="var(--teal)" stroke-width="2"/>
    </svg>

    <p class="card__tagline">The Tender Path</p>

    <div class="brand">
      <span class="brand__mark"></span>
      <span class="brand__name">Zarqa Fowl</span>
    </div>

    <h1 class="card__person">Tariq Moussef</h1>

    <ul class="contact">
      <li>Tel.: 07812450937</li>
      <li>E-mail: zarqa_fowl@mailbox-example.com</li>
      <li>Website: www.zarqafowl-example.com</li>
    </ul>
  </section>
</main>
</body>
</html>
```